Create a beautiful brochure for a Permanent Make Up Clinic

I need a classy brochure for my Permanent Make up Clinic. It needs a classy cover and the list of services and extra information on the inside. I don't have any requirements on size of the brochure, but it needs to look attractive and upmarket. The colors I like are black -white - Gold - grey. I like a minimalistic look.
I’d like to have my logo on the cover, the price list on the inside and the address information at the back.

Target Market(s)

woman between 18 and 99 years old

Industry/Entity Type

Beauty

Font styles to use
Sans Serif
Script

Colors

Designer to choose colors to be used in the design.

Requirements
Must have
• the logo on the cover
• pictures of the services with an explanation and pricing
• address information at the back
Nice to have
• a classy upmarket look, not with too many different colors in it.

```html
<!DOCTYPE html>
<html lang="nl">
<head>
<meta charset="utf-8">
<title>Lumé Clinic – brochure</title>
<link rel="stylesheet" href="https://fonts.googleapis.com/css2?family=Montserrat:wght@300;400;500;600;700&display=swap">
<style>
:root{
  --stage:#e6e6e6;
  --black:#111111;
  --ink:#1c1c1c;
  --white:#ffffff;
  --gold:#c6a25e;
  --gold-light:#dcc08a;
  --gold-dark:#a9853f;
  --grey:#8a8a8a;
  --grey-light:#bdbdbd;
  --text-dark:#444444;
}
*{margin:0;padding:0;box-sizing:border-box}
html,body{width:880px;height:1200px;overflow:hidden}
body{background:var(--stage);font-family:'Montserrat',sans-serif;position:relative}
.sheet{position:absolute;left:60px;width:760px;display:flex;box-shadow:0 6px 18px rgba(0,0,0,.25)}
.sheet--outside{top:50px;height:470px}
.sheet--inside{top:600px;height:550px}
.panel{position:relative;width:253.33px;height:100%;overflow:hidden}
.panel--black{background:var(--black);color:var(--grey-light)}
.panel--gold{background:linear-gradient(160deg,var(--gold-light),var(--gold) 55%,var(--gold-dark));color:var(--ink)}
.panel--white{background:var(--white);color:var(--text-dark)}
.photo{position:absolute}
.small{font-size:7px;line-height:1.55}

/* outside left */
.portrait{left:22px;top:22px;width:74px;height:74px;border-radius:50%;border:2px solid var(--gold);background:radial-gradient(circle at 50% 40%,#e9d6c4,#b89a83 70%,#6d5a4c)}
.intro{position:absolute;left:22px;right:22px;top:112px}
.intro p{margin-bottom:9px}
.intro .lead{color:var(--white)}
.eye-photo{left:0;right:0;bottom:0;height:190px;background:linear-gradient(135deg,#d8d8d8,#8c8c8c 50%,#3a3a3a)}
.gold-frame{position:absolute;left:14px;right:14px;bottom:14px;height:162px;border:1px solid var(--gold)}

/* outside middle */
.contact{position:absolute;inset:0;display:flex;flex-direction:column;align-items:center;text-align:center;padding:48px 24px 24px}
.contact h2{font-size:15px;font-weight:600;margin-bottom:8px}
.contact .phone{font-size:10px;font-weight:500;letter-spacing:.5px;margin-bottom:16px;display:flex;align-items:center;gap:5px}
.btn{background:var(--white);color:var(--ink);font-size:8px;font-weight:500;padding:6px 18px;border-radius:14px;margin-bottom:26px}
.logo{font-weight:500;letter-spacing:1px}
.contact .logo{font-size:20px;margin-bottom:6px}
.contact .address{font-size:8px;line-height:1.5;margin-bottom:12px}
.social{display:flex;gap:6px;margin-bottom:4px}
.social span{width:12px;height:12px;border-radius:50%;background:var(--ink)}
.contact .handle{font-size:7px}
.contact .web{margin-top:auto;font-size:8px;font-weight:500}

/* outside right */
.hands-photo{left:0;top:0;right:0;height:220px;background:linear-gradient(120deg,#f2f2f2,#a8a8a8 55%,#4a4a4a)}
.cover-logo{position:absolute;left:0;right:0;top:262px;text-align:center;color:var(--white);font-size:30px}
.tagline{position:absolute;left:60px;right:18px;top:360px;border:1px solid var(--gold);padding:10px 12px;text-align:right;color:var(--gold)}
.tagline .line1{font-size:12px;font-weight:400}
.tagline .line2{font-size:15px;font-weight:600;letter-spacing:.5px;line-height:1.2}

/* inside left */
.pmu-info{position:absolute;left:20px;right:20px;top:20px}
.pmu-info h2{color:var(--gold);font-size:14px;font-weight:600;line-height:1.25;margin-bottom:10px}
.pmu-info p{margin-bottom:7px}
.pmu-info h3{color:var(--gold-dark);font-size:8px;font-weight:600;margin:4px 0 6px}
.ticks{list-style:none}
.ticks li{display:flex;gap:5px;margin-bottom:5px}
.ticks svg{flex:none;margin-top:1px}
.face-photo{left:0;right:0;bottom:0;height:200px;background:linear-gradient(150deg,#f1ddd0,#d7a993 50%,#8f5f52)}

/* inside middle */
.services{position:absolute;left:18px;right:18px;top:20px}
.services h2{color:var(--white);font-size:10.5px;font-weight:600;margin-bottom:14px;line-height:1.35}
.service{margin-bottom:13px}
.service-head{display:flex;justify-content:space-between;align-items:center;margin-bottom:4px}
.service-name{color:var(--white);font-size:8px;font-weight:500}
.price{background:var(--gold);color:var(--black);font-size:7.5px;font-weight:600;padding:2px 7px}
.service p{color:var(--grey)}

/* inside right */
.brow-photo{left:0;right:0;top:0;height:170px;background:linear-gradient(130deg,#e8d3c2,#b48d77 55%,#5d4336)}
.detail-photo{left:0;right:0;top:170px;height:130px;background:linear-gradient(130deg,#dadada,#8f8f8f 60%,#505050)}
.consult{position:absolute;left:22px;right:22px;top:318px;border:1px solid var(--gold);background:var(--ink);color:var(--gold);text-align:center;font-size:10px;font-weight:600;letter-spacing:.8px;padding:8px 0}
.consult-text{position:absolute;left:22px;right:22px;top:362px}
.consult-text p{margin-bottom:8px}
.inside-web{position:absolute;left:0;right:0;bottom:22px;text-align:center;font-size:8px;font-weight:500;color:var(--ink)}
</style>
</head>
<body>

<section class="sheet sheet--outside">
  <div class="panel panel--black">
    <div class="photo portrait" role="img" aria-label="Portret van de eigenares van de kliniek"></div>
    <div class="intro small">
      <p class="lead">Bij Lumé Clinic staat jouw natuurlijke schoonheid centraal. Met jaren ervaring en oog voor detail zorgen wij voor een resultaat dat bij je past.</p>
      <p>Onze behandelingen worden uitgevoerd in een rustige, hygiënische omgeving met hoogwaardige pigmenten en moderne technieken.</p>
      <p>Wij nemen graag de tijd voor een persoonlijk gesprek.</p>
    </div>
    <div class="photo eye-photo" role="img" aria-label="Zwart-witfoto van een oog tijdens een permanente make-upbehandeling"></div>
    <div class="gold-frame"></div>
  </div>

  <div class="panel panel--gold">
    <div class="contact">
      <h2>Heb je nog vragen?</h2>
      <div class="phone">
        <svg width="9" height="9" viewBox="0 0 24 24"><path d="M6.6 10.8a15 15 0 0 0 6.6 6.6l2.2-2.2a1 1 0 0 1 1-.25 11.4 11.4 0 0 0 3.6.57 1 1 0 0 1 1 1V20a1 1 0 0 1-1 1A17 17 0 0 1 3 4a1 1 0 0 1 1-1h3.5a1 1 0 0 1 1 1c0 1.25.2 2.45.57 3.57a1 1 0 0 1-.25 1z" fill="#1c1c1c"/></svg>
        +32 470 12 34 56
      </div>
      <div class="btn">Schrijf je afspraak in</div>
      <div class="logo">Lumé Clinic</div>
      <div class="address">Lumé Clinic<br>Lindenlaan 14, 2500 Lier</div>
      <div class="social"><span></span><span></span></div>
      <div class="handle">@lumeclinic</div>
      <div class="web">www.lumeclinic.be</div>
    </div>
  </div>

  <div class="panel panel--black">
    <div class="photo hands-photo" role="img" aria-label="Zwart-witfoto van handen met handschoenen die een behandeling uitvoeren"></div>
    <div class="logo cover-logo">Lumé CLINIC</div>
    <div class="tagline">
      <div class="line1">Benadruk Je</div>
      <div class="line2">NATUURLIJKE<br>SCHOONHEID!</div>
    </div>
  </div>
</section>

<section class="sheet sheet--inside">
  <div class="panel panel--white">
    <div class="pmu-info small">
      <h2>Permanent Make Up, de behandeling die alles mooier maakt</h2>
      <p>Permanente make-up is een semi-permanente techniek waarbij pigment in de huid wordt aangebracht. Zo geniet je elke dag van een verzorgde look zonder moeite.</p>
      <h3>Wat zijn de voordelen voor jou?</h3>
      <ul class="ticks">
        <li><svg width="8" height="8" viewBox="0 0 10 10"><path d="M1 5l3 3 5-6" stroke="#c6a25e" stroke-width="1.6" fill="none"/></svg>Je bespaart elke ochtend tijd voor de spiegel.</li>
        <li><svg width="8" height="8" viewBox="0 0 10 10"><path d="M1 5l3 3 5-6" stroke="#c6a25e" stroke-width="1.6" fill="none"/></svg>Een natuurlijk resultaat dat perfect bij je gezicht past.</li>
        <li><svg width="8" height="8" viewBox="0 0 10 10"><path d="M1 5l3 3 5-6" stroke="#c6a25e" stroke-width="1.6" fill="none"/></svg>Geen uitgelopen make-up meer bij sport of zon.</li>
      </ul>
      <p>Het resultaat blijft twee tot drie jaar mooi en wordt steeds afgestemd op jouw wensen.</p>
    </div>
    <div class="photo face-photo" role="img" aria-label="Foto van een vrouw met verzorgde wenkbrauwen en lippen"></div>
  </div>

  <div class="panel panel--black">
    <div class="services">
      <h2>Wij bieden je de mooiste permanente make-up behandelingen</h2>
      <div class="service">
        <div class="service-head"><span class="service-name">Poeder Brows (Ombré Shading)</span><span class="price">€ 350</span></div>
        <p class="small">Zachte, gepoederde wenkbrauwen met een natuurlijk verloop van licht naar donker.</p>
      </div>
      <div class="service">
        <div class="service-head"><span class="service-name">Full Lips Aquarelle Techniek</span><span class="price">€ 300</span></div>
        <p class="small">Egale kleur en een mooie contour voor vollere, frisse lippen.</p>
      </div>
      <div class="service">
        <div class="service-head"><span class="service-name">Eyeliner techniek</span><span class="price">€ 250</span></div>
        <p class="small">Een subtiele of opvallende lijn die je ogen de hele dag laat stralen.</p>
      </div>
      <div class="service">
        <div class="service-head"><span class="service-name">Lash liner</span><span class="price">€ 200</span></div>
        <p class="small">Pigment tussen de wimpers voor een vollere wimperrand zonder zichtbare lijn.</p>
      </div>
      <div class="service">
        <div class="service-head"><span class="service-name">Bijwerking</span><span class="price">€ 150</span></div>
        <p class="small">Opfrissen van een bestaande behandeling binnen het jaar.</p>
      </div>
      <div class="service">
        <div class="service-head"><span class="service-name">Correctie vorige PMU</span><span class="price">€ 100</span></div>
        <p class="small">Aanpassing van kleur of vorm na advies en grondige analyse.</p>
      </div>
    </div>
  </div>

  <div class="panel panel--white">
    <div class="photo brow-photo" role="img" aria-label="Foto van een wenkbrauwbehandeling"></div>
    <div class="photo detail-photo" role="img" aria-label="Foto van een close-up na de behandeling"></div>
    <div class="consult">GRATIS ADVIESGESPREK</div>
    <div class="consult-text small">
      <p>Twijfel je nog? Tijdens een vrijblijvend adviesgesprek bespreken we samen je wensen, de mogelijkheden en het verwachte resultaat.</p>
      <p>Bel of mail ons en plan vandaag nog jouw afspraak in.</p>
    </div>
    <div class="inside-web">www.lumeclinic.be</div>
  </div>
</section>

</body>
</html>
```